Nirel Solutions Business Card
Stationary as well/logo for resumes, etc.
We are getting there. I need two samples...I like the black face Quorvix has going. I want the website across the bottom. I potentially want to see a black fade into a white bottom (background).
I also don't want it too busy so one color (blue) font. quorvix is close to what I am seeking
Gang,
I uploaded the files of my logo and am sorry for doing this late. What I am looking for is a business card and staionary that incorporates this. Peltcraft you are close to what I am lookign for witht he staionary- the card layout, I like tobrenik's better. In my logo there is a two tone as well, some with a black background and some with white- i want to try and explore this...

```html
<!DOCTYPE html>
<html lang="en">
<head>
<meta charset="utf-8">
<title>Nirel Solutions Business Card</title>
<link href="https://fonts.googleapis.com/css2?family=Arimo:wght@400;700&display=swap" rel="stylesheet">
<style>
  :root {
    --backdrop: #2b2b2b;
    --card-dark: #151515;
    --card-mid: #6d6d6d;
    --card-light: #f2f2f2;
    --text-light: #ffffff;
    --text-soft: #e6e6e6;
    --web-grey: #555555;
    --brand-blue: #2a9fc4;
    --mark-grey: #c9c9c9;
  }
  html, body {
    margin: 0;
    width: 1200px;
    height: 910px;
    overflow: hidden;
    background: var(--backdrop);
    font-family: "Arimo", Arial, sans-serif;
  }
  .business-card {
    position: absolute;
    left: 128px;
    top: 192px;
    width: 947px;
    height: 504px;
    background: linear-gradient(105deg, var(--card-dark) 0%, var(--card-mid) 38%, var(--card-light) 68%, #ffffff 100%);
    box-shadow: 0 6px 24px rgba(0,0,0,0.45);
    color: var(--text-light);
  }
  .holder-name {
    position: absolute;
    left: 44px;
    top: 36px;
    margin: 0;
    font-size: 32px;
    font-weight: 700;
    letter-spacing: 0.5px;
  }
  .holder-title {
    position: absolute;
    left: 44px;
    top: 78px;
    margin: 0;
    font-size: 20px;
    color: var(--text-soft);
  }
  .office-address {
    position: absolute;
    left: 44px;
    top: 136px;
    margin: 0;
    font-size: 26px;
    line-height: 31px;
    font-style: normal;
  }
  .contact-list {
    position: absolute;
    left: 44px;
    top: 258px;
    margin: 0;
    font-size: 23px;
    line-height: 39px;
    display: grid;
    grid-template-columns: 112px 20px auto;
  }
  .contact-list dt, .contact-list dd { margin: 0; }
  .website {
    position: absolute;
    left: 0;
    width: 1000px;
    top: 440px;
    text-align: center;
    font-size: 34px;
    font-weight: 700;
    letter-spacing: 1.5px;
    color: var(--web-grey);
    padding-left: 50px;
    box-sizing: border-box;
  }
  .brand-mark {
    position: absolute;
    left: 611px;
    top: 20px;
    width: 220px;
    height: 220px;
  }
  .brand-name {
    position: absolute;
    left: 520px;
    top: 300px;
    width: 410px;
    margin: 0;
    text-align: center;
    font-size: 44px;
    font-weight: 700;
    letter-spacing: 3px;
    color: var(--brand-blue);
  }
</style>
</head>
<body>
  <section class="business-card">
    <h1 class="holder-name">Dorian K. Ashfield</h1>
    <p class="holder-title">Business Developer Manager</p>
    <address class="office-address">1840 Crestline Avenue<br>Suite 200<br>Houston, TX 77027</address>
    <dl class="contact-list">
      <dt>Phone</dt><dd>:</dd><dd>713.555.0148</dd>
      <dt>Cell</dt><dd>:</dd><dd>713.555.0172</dd>
      <dt>Fax</dt><dd>:</dd><dd>713.555.0193</dd>
      <dt>E-mail</dt><dd>:</dd><dd>dorian@nirel-it.com</dd>
    </dl>
    <svg class="brand-mark" viewBox="0 0 220 220" aria-hidden="true">
      <circle cx="110" cy="110" r="108" fill="var(--mark-grey)"/>
    </svg>
    <p class="brand-name">NIREL SOLUTIONS</p>
    <div class="website">www.nirel-it.com</div>
  </section>
</body>
</html>
```